BrackenfieldGoods.com

I need a site that I can sell dewatering equipment to the construction industry.
Ie, pipes fittings pumps and other such things needed to remove the groundwater on construction sites. Here in Florida, it’s needed almost everywhere seeing we are at sea level.
I want to be able to sell these products on the site and receive

Coding

Coded - Design and coding required

Number of Pages Required

1 page

```html
<!DOCTYPE html>
<html lang="en">
<head>
<meta charset="utf-8">
<title>Brackenfield Goods LLC</title>
<link href="https://fonts.googleapis.com/css2?family=Ubuntu:wght@400;500;700&family=Open+Sans:wght@400;600;700&family=Noto+Serif&display=swap" rel="stylesheet">
<style>
:root{
  --navy:#1a3d7c;
  --blue:#3a9be0;
  --blue-dark:#1b5e96;
  --ink:#1e1e1e;
  --muted:#8a8a8a;
  --light:#f4f5f7;
  --line:#e3e5e8;
  --footer:#1f1f21;
  --footer-bar:#151516;
  --white:#ffffff;
}
*{box-sizing:border-box;margin:0;padding:0}
html,body{width:1200px;height:2597px;overflow:hidden}
body{position:relative;font-family:"Open Sans",sans-serif;color:var(--ink);background:var(--white)}
.abs{position:absolute}
h1,h2,h3,h4{font-family:"Ubuntu",sans-serif}

/* header */
.header{top:0;left:0;width:1200px;height:142px}
.brand{left:161px;top:30px;font:700 25px "Ubuntu",sans-serif;color:var(--navy);letter-spacing:.3px}
.info{display:flex;align-items:center;gap:12px;font-size:11px;line-height:15px;color:#444}
.info .ico{width:30px;height:30px;border-radius:50%;background:#eef3f8;display:flex;align-items:center;justify-content:center}
.info-address{left:638px;top:30px}
.info-contact{left:848px;top:30px}
.info-contact .phone{color:var(--blue)}
.divider{left:822px;top:28px;width:1px;height:34px;border-left:1px dashed #ccc}
.nav{left:161px;top:94px;width:880px;height:48px;background:var(--blue);overflow:hidden}
.nav ul{list-style:none;display:flex;height:48px;align-items:center;padding-left:22px}
.nav li{font:700 10.5px "Open Sans",sans-serif;color:var(--white);letter-spacing:.4px;padding-right:18px;margin-right:18px;border-right:1px dotted rgba(255,255,255,.8);line-height:14px}
.nav .corner{right:0;top:0;width:0;height:0;border-top:44px solid var(--blue-dark);border-left:44px solid transparent}
.nav .cart{right:50px;top:13px}

/* hero */
.hero{top:142px;left:0;width:1200px;height:397px;background:linear-gradient(180deg,#dfe8df 0%,#a9c49a 50%,#8fb07b 100%)}
.hero-title{left:0;top:168px;width:1200px;text-align:center;font:700 48px "Ubuntu",sans-serif;color:var(--navy);letter-spacing:2px}
.hero-title span{display:inline-block;border-top:2px solid var(--navy);border-bottom:2px solid var(--navy);padding:0 4px;line-height:58px}

/* products */
.section-title{width:1200px;left:0;text-align:center;font:700 23px "Ubuntu",sans-serif;letter-spacing:1px}
.section-sub{width:1200px;left:0;text-align:center;font:600 12px "Open Sans",sans-serif;color:#333}
.card{width:187px;height:241px;background:var(--white);box-shadow:0 1px 6px rgba(0,0,0,.15);overflow:hidden}
.card .corner{right:0;top:0;border-top:36px solid var(--blue-dark);border-left:36px solid transparent;width:0;height:0}
.card .thumb{left:15px;top:26px;width:157px;height:138px}
.card h4{left:21px;top:176px;font:500 13px "Ubuntu",sans-serif;white-space:nowrap}
.card p{left:21px;top:196px;width:110px;font-size:10px;line-height:15px;color:var(--muted)}
.card .bag{right:20px;top:202px}
.arrow{width:26px;height:26px;border-radius:3px;display:flex;align-items:center;justify-content:center}
.arrow-prev{left:131px;top:801px;background:var(--blue-dark)}
.arrow-next{left:1040px;top:801px;background:#e8e8e8}

/* pumps */
.pumps{top:991px;left:0;width:1200px;height:516px;background-color:var(--light);background-image:radial-gradient(#dcdfe3 1px,transparent 1.5px);background-size:46px 46px}
.pumps h2{left:160px;top:68px;font:700 25px "Ubuntu",sans-serif;letter-spacing:1px}
.pumps .lead{left:160px;top:101px;width:360px;font:600 13px/19px "Open Sans",sans-serif;color:#333}
.feature-icon{width:70px;height:70px;border-radius:50%}
.fi-1{left:160px;top:184px;border:2px solid var(--blue);background:var(--white)}
.fi-2{left:166px;top:313px;width:60px;height:60px;background:var(--white);box-shadow:0 1px 4px rgba(0,0,0,.1)}
.feature h3{font:700 13.5px/17px "Ubuntu",sans-serif;letter-spacing:.6px}
.feature p{margin-top:8px;font:11px/18px "Noto Serif",serif;color:#444}
.feature-1{left:240px;top:190px;width:260px}
.feature-2{left:240px;top:313px;width:260px}
.pump-photo{left:520px;top:142px;width:242px;height:374px;background:linear-gradient(180deg,#3a3a3c 0%,#2a2a2c 35%,#2f9ad6 60%,#1f86c4 80%,#2a2a2c 100%);border-radius:30px 30px 10px 10px}
.form{left:779px;top:78px;width:262px;height:372px;background:var(--white);box-shadow:0 2px 8px rgba(0,0,0,.15);overflow:hidden}
.form .corner{right:0;top:0;width:0;height:0;border-top:78px solid var(--blue-dark);border-left:78px solid transparent}
.form h3{left:15px;top:36px;font:700 16px "Ubuntu",sans-serif;letter-spacing:.6px}
.field{left:15px;width:232px;height:37px;border:1px solid var(--line);font-size:9px;color:#999;padding:12px 10px}
.form .send{left:148px;top:310px;width:98px;height:36px;background:var(--blue);color:var(--white);font:700 10px/36px "Open Sans",sans-serif;text-align:center;letter-spacing:.6px}

/* about */
.about{top:1507px;left:0;width:1200px;height:273px}
.about .big{left:160px;top:56px;font:700 45px/52px "Ubuntu",sans-serif;color:var(--blue);letter-spacing:4px}
.about .tag{left:160px;top:162px;font:700 28px "Ubuntu",sans-serif;color:var(--ink);letter-spacing:1px}
.about h4{left:600px;top:66px;font:700 12px "Open Sans",sans-serif}
.about p{left:600px;top:90px;font-size:12px;line-height:20px;color:#444;white-space:nowrap}
.quote-btn{left:600px;top:144px;width:232px;height:60px;background:var(--blue);color:var(--white);font:700 13px/60px "Open Sans",sans-serif;text-align:center;letter-spacing:.6px;border-radius:3px}

/* testimonials */
.testi{top:1780px;left:0;width:1200px;height:347px;background:linear-gradient(180deg,#8d9196 0%,#9a9ea2 50%,#7c8086 100%)}
.testi h2{left:0;top:50px;width:1200px;text-align:center;font:700 25px "Ubuntu",sans-serif;color:var(--white);letter-spacing:1px}
.tcard{top:120px;width:374px;height:128px;background:var(--white);overflow:hidden}
.tcard .corner{right:0;top:0;width:0;height:0;border-top:52px solid var(--blue-dark);border-left:52px solid transparent}
.tcard .avatar{left:14px;top:14px;width:94px;height:86px;background:linear-gradient(180deg,#dfe4ea,#b9c4cf)}
.tcard .q{left:122px;top:8px;font:700 30px/30px "Ubuntu",sans-serif;color:#ccc}
.tcard p{left:122px;top:34px;font-size:10px;line-height:16px;color:#999;white-space:nowrap}
.tcard .stars{left:122px;top:74px}
.pager{top:290px;width:26px;height:26px;font:600 11px/26px "Open Sans",sans-serif;text-align:center;border-radius:2px}
.pager-1{left:570px;background:var(--blue-dark);color:var(--white)}
.pager-2{left:604px;background:var(--white);color:#333}

/* footer */
.footer{top:2127px;left:0;width:1200px;height:419px;background:var(--footer);color:#ddd}
.footer-pump{left:70px;top:62px;width:320px;height:300px;border-radius:40px;background:linear-gradient(150deg,#49c4d8 0%,#1c9bb4 55%,#0e6f84 100%)}
.footer h4{font:700 12px "Ubuntu",sans-serif;color:var(--white);letter-spacing:.6px}
.footer h4::after{content:"";display:block;width:26px;height:2px;background:var(--blue);margin-top:8px}
.fh-form{left:419px;top:46px}
.finput{top:86px;height:35px;background:#3a3a3d;font-size:9px;color:#999;padding:12px 10px}
.fsend{left:944px;top:86px;width:69px;height:35px;background:var(--blue);color:var(--white);font:700 10px/35px "Open Sans",sans-serif;text-align:center;letter-spacing:.6px}
.fh-nav{left:426px;top:164px}
.fh-contact{left:637px;top:164px}
.flist{list-style:none;font-size:11px;line-height:24px;color:#e6e6e6}
.flist-nav{left:426px;top:206px}
.flist-contact{left:637px;top:206px}
.social{top:342px;width:24px;height:24px;background:#3a3a3d}
.copyright{top:2546px;left:0;width:1200px;height:51px;background:var(--footer-bar);color:#777;font-size:10px;line-height:51px;text-align:center}
</style>
</head>
<body>

<header class="header abs">
  <div class="brand abs">BRACKENFIELD GOODS LLC</div>
  <div class="info info-address abs">
    <span class="ico"><svg width="12" height="12" viewBox="0 0 12 12"><path d="M6 1 L11 6 H9.5 V11 H7 V8 H5 V11 H2.5 V6 H1 Z" fill="#3a9be0"/></svg></span>
    <span>LOREM IPSUM DOLOR<br>SIT AMET CONSECTETOR</span>
  </div>
  <div class="divider abs"></div>
  <div class="info info-contact abs">
    <span class="ico"><svg width="12" height="12" viewBox="0 0 12 12"><path d="M2.5 1 L4.5 1 L5.5 3.8 L4.2 4.8 C4.9 6.3 5.8 7.2 7.2 7.8 L8.2 6.5 L11 7.5 L11 9.5 C11 10.3 10.3 11 9.5 11 C5 11 1 7 1 2.5 C1 1.7 1.7 1 2.5 1 Z" fill="#3a9be0"/></svg></span>
    <span><span class="phone">+10 (123) 456 789</span><br>info@brackenfieldgoods.com</span>
  </div>
  <nav class="nav abs">
    <ul>
      <li>DEWATERING</li>
      <li>PUMPS &amp; EQUIPMENT</li>
      <li>GROUNDWATER CONTROL BLOG</li>
      <li>SUPPORT</li>
      <li>ABOUT</li>
    </ul>
    <svg class="cart abs" width="22" height="22" viewBox="0 0 22 22" aria-label="Cart"><path d="M4 7 H16 L15 19 H5 Z" fill="none" stroke="#fff" stroke-width="1.8"/><path d="M7 7 V5 A3 3 0 0 1 13 5 V7" fill="none" stroke="#fff" stroke-width="1.8"/><circle cx="16" cy="16" r="4.5" fill="#fff"/><path d="M14 16 H18 M16 14 V18" stroke="#3a9be0" stroke-width="1.5"/></svg>
    <div class="corner abs"></div>
  </nav>
</header>

<section class="hero abs" role="img" aria-label="Trailer-mounted dewatering pumps with yellow pipes on a grassy site">
  <h1 class="hero-title abs"><span>BRACKENFIELD GOODS</span></h1>
</section>

<section class="products">
  <h2 class="section-title abs" style="top:600px">OUR PRODUCTS</h2>
  <div class="section-sub abs" style="top:634px">Lorem Ipsum Dolor Sit Amet Consectetor</div>

  <div class="arrow arrow-prev abs"><svg width="8" height="10" viewBox="0 0 8 10"><path d="M6 1 L2 5 L6 9 Z" fill="#fff"/></svg></div>
  <div class="arrow arrow-next abs"><svg width="8" height="10" viewBox="0 0 8 10"><path d="M2 1 L6 5 L2 9 Z" fill="#333"/></svg></div>

  <article class="card abs" style="left:189px;top:694px">
    <div class="thumb abs" role="img" aria-label="Wellpoint hose and fitting on pavement" style="background:linear-gradient(135deg,#8a8478,#b7b1a5)"></div>
    <h4 class="abs">Wellpoint Standard</h4>
    <p class="abs">Lorem ipsum dolor sit amet, consectetur</p>
    <svg class="bag abs" width="16" height="16" viewBox="0 0 16 16"><rect x="2" y="5" width="12" height="10" fill="none" stroke="#333" stroke-width="1.4"/><path d="M5 5 V3.5 A3 3 0 0 1 11 3.5 V5" fill="none" stroke="#333" stroke-width="1.4"/></svg>
    <div class="corner abs"></div>
  </article>
  <article class="card abs" style="left:400px;top:694px">
    <div class="thumb abs" role="img" aria-label="Black siphon well adapter" style="background:linear-gradient(135deg,#c9c4ba,#8f8a82)"></div>
    <h4 class="abs">Siphon Well Adapter</h4>
    <p class="abs">Lorem ipsum dolor sit amet, consectetur</p>
    <svg class="bag abs" width="16" height="16" viewBox="0 0 16 16"><rect x="2" y="5" width="12" height="10" fill="none" stroke="#333" stroke-width="1.4"/><path d="M5 5 V3.5 A3 3 0 0 1 11 3.5 V5" fill="none" stroke="#333" stroke-width="1.4"/></svg>
    <div class="corner abs"></div>
  </article>
  <article class="card abs" style="left:611px;top:694px">
    <div class="thumb abs" role="img" aria-label="Blue wellpoint tip" style="background:linear-gradient(135deg,#9aa1a8,#4f8fc7)"></div>
    <h4 class="abs">Harrow MFG - Wellpoint</h4>
    <p class="abs">Lorem ipsum dolor sit amet, consectetur</p>
    <svg class="bag abs" width="16" height="16" viewBox="0 0 16 16"><rect x="2" y="5" width="12" height="10" fill="none" stroke="#333" stroke-width="1.4"/><path d="M5 5 V3.5 A3 3 0 0 1 11 3.5 V5" fill="none" stroke="#333" stroke-width="1.4"/></svg>
    <div class="corner abs"></div>
  </article>
  <article class="card abs" style="left:822px;top:694px">
    <div class="thumb abs" role="img" aria-label="Yellow PVC header pipe plug" style="background:radial-gradient(circle at 50% 40%,#f4d11a 0%,#e5b800 35%,#111 70%)"></div>
    <h4 class="abs">PVC Header Pipe Plug</h4>
    <p class="abs">Lorem ipsum dolor sit amet, consectetur</p>
    <svg class="bag abs" width="16" height="16" viewBox="0 0 16 16"><rect x="2" y="5" width="12" height="10" fill="none" stroke="#333" stroke-width="1.4"/><path d="M5 5 V3.5 A3 3 0 0 1 11 3.5 V5" fill="none" stroke="#333" stroke-width="1.4"/></svg>
    <div class="corner abs"></div>
  </article>
</section>

<section class="pumps abs">
  <h2 class="abs">PUMPS &amp; EQUIPMENTS</h2>
  <p class="lead abs">Lorem ipsum dolor sit amet, consectetur adipiscing elit, sed do eiusmod tempor incididunt ut.</p>

  <div class="feature-icon fi-1 abs"><svg width="66" height="66" viewBox="0 0 66 66"><rect x="18" y="24" width="22" height="18" fill="none" stroke="#3a9be0" stroke-width="2"/><path d="M40 30 H50 V36 H40 M23 24 V18 H35 V24" fill="none" stroke="#3a9be0" stroke-width="2"/></svg></div>
  <div class="feature feature-1 abs">
    <h3>PIPES FITTINGS PUMPS</h3>
    <p>Lorem ipsum dolor sit amet, consectetur adipiscing elit, sed do eiusmod tempor incididunt ut labore et dolore magna aliqua.</p>
  </div>

  <div class="feature-icon fi-2 abs"><svg width="60" height="60" viewBox="0 0 60 60"><rect x="18" y="24" width="20" height="13" rx="2" fill="none" stroke="#555" stroke-width="1.6"/><path d="M38 28 H44 V33 H38 M22 24 V21 M34 24 V21" fill="none" stroke="#555" stroke-width="1.6"/></svg></div>
  <div class="feature feature-2 abs">
    <h3>REMOVE THE GROUNDWATER ON CONSTRUCTION SITES</h3>
    <p>Duis aute irure dolor in reprehenderit in voluptate velit esse cillum dolore eu fugiat nulla pariatur. Excepteur sint occaecat cupidatat non proident, sunt in</p>
  </div>

  <div class="pump-photo abs" role="img" aria-label="Black and blue electric submersible pump"></div>

  <form class="form abs">
    <h3 class="abs">SUBMISSION FORM</h3>
    <div class="field abs" style="top:74px">Name</div>
    <div class="field abs" style="top:119px">Email</div>
    <div class="field abs" style="top:164px">Phone</div>
    <div class="field abs" style="top:209px;height:82px">Your Message</div>
    <div class="send abs">SUBMIT</div>
    <div class="corner abs"></div>
  </form>
</section>

<section class="about abs">
  <div class="big abs">BRACKENFIELD<br>GOODS LLC</div>
  <div class="tag abs">GROUNDWATER CONTROL</div>
  <h4 class="abs">About Us</h4>
  <p class="abs">Lorem ipsum dolor sit amet, consectetur adipiscing elit, sed do eiusmod<br>tempor incididunt ut labore et dolore magna aliqua. Lorem ipsum dolor sit</p>
  <div class="quote-btn abs">BOOK FOR A QUOTE</div>
</section>

<section class="testi abs" role="img" aria-label="Faded background of portable water pumps">
  <h2 class="abs">WHAT OUR CLIENT SAYS</h2>
  <article class="tcard abs" style="left:189px">
    <div class="avatar abs" role="img" aria-label="Client portrait"></div>
    <div class="q abs">&ldquo;</div>
    <p class="abs">Lorem ipsum dolor sit amet, consectetur adipi-<br>scing elit, sed do eiusmod tempor incididunt</p>
    <svg class="stars abs" width="80" height="14" viewBox="0 0 80 14"><g fill="#3a9be0"><path id="s" d="M7 0 L8.8 4.6 L13.7 5 L10 8.2 L11.1 13 L7 10.4 L2.9 13 L4 8.2 L0.3 5 L5.2 4.6 Z"/><use href="#s" x="16"/><use href="#s" x="32"/><use href="#s" x="48"/></g><use href="#s" x="64" fill="#ccc"/></svg>
    <div class="corner abs"></div>
  </article>
  <article class="tcard abs" style="left:639px">
    <div class="avatar abs" role="img" aria-label="Client portrait"></div>
    <div class="q abs">&ldquo;</div>
    <p class="abs">Lorem ipsum dolor sit amet, consectetur adipi-<br>scing elit, sed do eiusmod tempor incididunt</p>
    <svg class="stars abs" width="80" height="14" viewBox="0 0 80 14"><g fill="#3a9be0"><path id="s2" d="M7 0 L8.8 4.6 L13.7 5 L10 8.2 L11.1 13 L7 10.4 L2.9 13 L4 8.2 L0.3 5 L5.2 4.6 Z"/><use href="#s2" x="16"/><use href="#s2" x="32"/><use href="#s2" x="48"/></g><use href="#s2" x="64" fill="#ccc"/></svg>
    <div class="corner abs"></div>
  </article>
  <div class="pager pager-1 abs">1</div>
  <div class="pager pager-2 abs">2</div>
</section>

<footer class="footer abs">
  <div class="footer-pump abs" role="img" aria-label="Turquoise centrifugal water pump"></div>
  <h4 class="fh-form abs">CONTACT FORM</h4>
  <div class="finput abs" style="left:419px;width:151px">Name</div>
  <div class="finput abs" style="left:577px;width:164px">Email</div>
  <div class="finput abs" style="left:748px;width:189px">Message</div>
  <div class="fsend abs">SEND</div>

  <h4 class="fh-nav abs">NAVIGATIONS</h4>
  <ul class="flist flist-nav abs">
    <li>Home</li><li>Dewatering</li><li>Pumps &amp; Equipments</li><li>Groundwater Control Blog</li><li>Support</li><li>About</li>
  </ul>
  <h4 class="fh-contact abs">CONTACT</h4>
  <ul class="flist flist-contact abs">
    <li style="line-height:15px;margin-bottom:7px">Lorem Ipsum Dolor Sit Amet Consectetor<br>Suite Sit Amet Lorem</li>
    <li>Phone: +00 (123) 456 789</li>
    <li>Fax: +00 1234 213</li>
    <li>Email: info@brackenfieldgoods.com</li>
  </ul>
  <div class="social abs" style="left:911px"></div>
  <div class="social abs" style="left:944px"></div>
  <div class="social abs" style="left:978px"></div>
  <div class="social abs" style="left:1013px"></div>
</footer>
<div class="copyright abs">&copy; Copyright 2018 Brackenfield Goods. All Rights Reserved.</div>

</body>
</html>
```